Business Card Design

Professional solutions in (servers, security, networks, programming)

Industry/Entity Type

Business

Contact Information for Business Card

Tarek Hounayni
Internet services and network solutions
DPV - RTLK - RTLB
netcare@qo-lam.com / 05917406238
www.qo-lam.com

```html
<!DOCTYPE html>
<html lang="en">
<head>
<meta charset="UTF-8">
<title>Tarek Hounayni — Business Card</title>
<link rel="stylesheet" href="https://fonts.googleapis.com/css2?family=Cinzel:wght@400;500&family=Cormorant+SC:wght@500;600&display=swap">
<style>
  :root {
    --backdrop: #d9dadc;
    --card: #ffffff;
    --ink-blue: #1d5596;
    --accent-gold: #e0b43c;
  }
  html, body {
    margin: 0;
    padding: 0;
    width: 1200px;
    height: 800px;
    overflow: hidden;
    background: var(--backdrop);
  }
  .stage {
    width: 1200px;
    height: 800px;
    display: flex;
    align-items: center;
    justify-content: center;
  }
  .business-card {
    width: 700px;
    height: 400px;
    background: var(--card);
    box-shadow: 0 10px 30px rgba(0, 0, 0, 0.18);
    display: flex;
    flex-direction: column;
    align-items: center;
    justify-content: center;
    color: var(--ink-blue);
    text-align: center;
  }
  .holder-name {
    font-family: "Cinzel", serif;
    font-weight: 500;
    font-size: 42px;
    letter-spacing: 1px;
    margin: 0;
    line-height: 1;
  }
  .name-rule {
    width: 330px;
    height: 2px;
    background: var(--accent-gold);
    margin: 12px 0 16px 70px;
  }
  .details {
    font-family: "Cormorant SC", serif;
    font-weight: 600;
    font-size: 19px;
    letter-spacing: 0.6px;
    line-height: 1.85;
    margin: 0;
  }
  .details p { margin: 0; }
</style>
</head>
<body>
  <main class="stage">
    <section class="business-card">
      <h1 class="holder-name">Tarek Hounayni</h1>
      <div class="name-rule"></div>
      <div class="details">
        <p class="services">Internet services and network solutions</p>
        <p class="credentials">DPV - RTLK - RTLB</p>
        <p class="contact">netcare@qo-lam.com / 05917406238</p>
        <p class="website">www.qo-lam.com</p>
      </div>
    </section>
  </main>
</body>
</html>
```